Keelbrook Vault Holdings Needs A Website

We are looking for a website for a new company. 4 Pages

Needs to be responsive and mobile friendly for all browsers and coded for both Android & IOS. SEO is also important.

Website Brief – Keelbrook Vault Holdings
Domain: www.keelbrookvault.net
Email: info@keelbrookvault.net
Phone: to be inserted later
Address: 40837 52 Ave, Edmonton, AB T6K 3R8
Platform: WordPress (recommended for flexibility, SEO tools, and ease of editing)
Requirements:
• Responsive & mobile-friendly (Android & iOS)
• Cross-browser compatibility
• Fast page load speed
• SEO optimized for storage development, management, and investment keywords
• Easy in-house editing after launch
• Professional, modern, trust-driven design reflecting expertise, reliability, and innovation
________________________________________
Pages
1. HOME
Purpose: Quickly communicate who Keelbrook Vault Holdings is and why they’re the best choice for designing, building, leasing, and managing self storage facilities.
Content Highlights:
• Hero Section: Large, bold image of a modern self storage facility with headline:
"From Concept to Capacity – Your Self Storage Experts"
• Subheadline: “Keelbrook Vault Holdings delivers turnkey design, construction, leasing, and management services for profitable self storage operations.”
• Quick Service Icons:
o Facility Design & Development
o Construction & Build Management
o Lease-Up & Marketing
o Ongoing Facility Management
• Call to Action Button: “LEARN MORE” → links to ABOUT US page.
• Featured Project Highlights: Showcase a few completed or current projects with photos and stats.
• Contact Banner: “Ready to build your next self storage project? Let’s talk.” → CONTACT page.
2. ABOUT US
Purpose: Build credibility, showcase experience, and explain the value proposition.
Content Highlights:
• Who We Are: Overview of Keelbrook Vault Holdings’ history, mission, and team expertise.
• Our Approach: End-to-end process from site selection to occupancy.
• Why Choose Us:
o Industry expertise in self storage
o Proven track record in lease-up success
o Strong vendor and contractor network
3. SERVICES
Purpose: Detail all service offerings with clarity and authority.
Sections:
• Design & Development: Market analysis, site planning, and architectural design.
• Construction Management: Overseeing timelines, budgets, and quality control.
• Lease-Up Strategy: Marketing, promotions, and occupancy acceleration.
• Ongoing Facility Management: Staffing, maintenance, revenue optimization.

4. CONTACT
Purpose: Provide simple, direct ways to connect.
Content Highlights:
• Contact Form (Name, Email, Phone, Message)
• Direct Email: info@keelbrookvault.net
• Phone (if applicable)
• Google Map embed (if there’s a head office location)
• CTA: “Let’s Build Your Storage Success Story.”
Design & Technical Notes
• Visual Style: Clean, modern, bold typography, professional color palette (to be based on branding), strong imagery of self storage facilities.
• Performance: Image compression, caching, responsive scaling.
• SEO Targets: “Self storage facility developer,” “self storage construction,” “self storage management company,” “lease-up services for self storage.”

WordPress or Joomla – must be desktop and mobile friendly with fast page load speed. Need the ability to edit ourselves.

Use pantone colours - #033c5a – dark blue
#2baadf – light blue

```html
<!DOCTYPE html>
<html lang="en">
<head>
<meta charset="utf-8">
<title>Keelbrook Vault Holdings – Self Storage Experts</title>
<link rel="stylesheet" href="https://fonts.googleapis.com/css2?family=Montserrat:wght@400;500;600;700;800&family=Open+Sans:wght@400;600&display=swap">
<style>
:root{
  --navy:#033c5a;
  --navy-deep:#062536;
  --sky:#2baadf;
  --sky-soft:#d8eef8;
  --ink:#0d2a3b;
  --grey:#5b6a75;
  --white:#ffffff;
}
*{box-sizing:border-box;margin:0;padding:0}
html,body{width:1200px;height:2676px;overflow:hidden}
body{position:relative;background:var(--white);font-family:"Open Sans",sans-serif;color:var(--ink)}

/* Header */
.site-header{position:absolute;top:0;left:0;width:1200px;height:56px;z-index:5;display:flex;align-items:center;padding:0 120px;background:rgba(3,30,46,.55)}
.brand{display:flex;align-items:center;gap:10px;font-family:"Montserrat",sans-serif;font-weight:700;color:var(--white);font-size:17px;white-space:nowrap}
.brand-mark{width:22px;height:22px;background:var(--sky);flex:none}
.main-nav{margin-left:auto;display:flex;gap:28px;font-family:"Montserrat",sans-serif;font-size:13px;font-weight:500;color:var(--white)}
.main-nav .active{color:var(--sky);border-bottom:2px solid var(--sky);padding-bottom:3px}
.btn{display:inline-flex;align-items:center;gap:8px;font-family:"Montserrat",sans-serif;font-weight:600;font-size:13px;border-radius:4px;padding:11px 20px;color:var(--white);text-decoration:none}
.btn-dark{background:var(--navy)}
.btn-sky{background:var(--sky)}
.btn-header{margin-left:36px;background:var(--navy-deep);padding:10px 18px}

/* Hero */
.hero-strip{position:absolute;top:0;left:0;width:1200px;height:612px;background:var(--sky);clip-path:polygon(0 0,100% 0,100% 88%,50% 100%,0 88%)}
.hero{position:absolute;top:0;left:0;width:1200px;height:598px;clip-path:polygon(0 0,100% 0,100% 87%,50% 100%,0 87%);overflow:hidden}
.hero-photo{position:absolute;inset:0;background:linear-gradient(110deg,#1b3444 0%,#46606f 40%,#8fa3ae 70%,#c6d1d7 100%)}
.hero-shade{position:absolute;inset:0;background:linear-gradient(90deg,rgba(3,32,50,.92) 0%,rgba(3,40,62,.7) 45%,rgba(3,40,62,.1) 80%)}
.hero-copy{position:absolute;left:120px;top:112px;width:560px;color:var(--white)}
.hero-copy h1{font-family:"Montserrat",sans-serif;font-weight:800;font-size:42px;line-height:1.18}
.hero-copy p{margin-top:22px;font-size:14px;line-height:1.6;width:470px}
.hero-copy .btn{margin-top:24px}
.hero-badge{position:absolute;top:566px;left:578px;width:44px;height:44px;border-radius:50%;background:var(--navy);border:3px solid var(--white);display:flex;align-items:center;justify-content:center;z-index:3}

/* Services */
.section-title{font-family:"Montserrat",sans-serif;font-weight:700;font-size:36px;color:var(--navy);text-align:center}
.services{position:absolute;top:652px;left:0;width:1200px;text-align:center}
.service-list{display:flex;justify-content:center;gap:40px;margin-top:46px}
.service{width:230px;display:flex;flex-direction:column;align-items:center}
.hex{width:80px;height:88px;background:var(--navy);clip-path:polygon(50% 0,100% 25%,100% 75%,50% 100%,0 75%,0 25%);display:flex;align-items:center;justify-content:center}
.service h3{margin-top:18px;font-family:"Montserrat",sans-serif;font-weight:700;font-size:17px;color:var(--ink);line-height:1.3}
.services .btn{margin-top:34px}

/* About */
.about{position:absolute;top:980px;left:0;width:1200px;height:580px;clip-path:polygon(0 12%,100% 0,100% 88%,0 100%);background:linear-gradient(180deg,#bfe3f3 0%,#9fd2ea 100%)}
.about-photo{position:absolute;right:0;top:0;width:760px;height:100%;background:linear-gradient(100deg,rgba(191,227,243,1) 0%,rgba(160,196,214,.55) 40%,rgba(120,160,182,.6) 100%)}
.about-copy{position:absolute;left:120px;top:130px;width:560px;color:var(--ink)}
.about-copy h2{font-family:"Montserrat",sans-serif;font-weight:700;font-size:36px;color:var(--navy)}
.about-copy p{margin-top:16px;font-size:13.5px;line-height:1.65}
.about-copy .btn{margin-top:22px}

/* Projects */
.projects{position:absolute;top:1572px;left:0;width:1200px;height:400px;text-align:center}
.projects .lead{margin:14px auto 0;width:560px;font-size:13.5px;line-height:1.55;color:var(--grey)}
.project-row{position:absolute;top:132px;left:120px;display:flex;gap:30px;text-align:left}
.project{width:300px;background:var(--white);box-shadow:0 4px 14px rgba(3,60,90,.15)}
.project-photo{height:160px}
.project-meta{display:flex;justify-content:space-between;margin:10px 12px 0;font-size:11px;color:var(--sky);font-weight:600}
.project h3{margin:6px 12px 16px;font-family:"Montserrat",sans-serif;font-weight:600;font-size:17px;line-height:1.3;color:var(--ink)}
.slider-arrow{position:absolute;top:250px;width:30px;height:30px;border-radius:50%;border:1px solid #b9c5cc;display:flex;align-items:center;justify-content:center;background:var(--white)}

/* CTA */
.cta{position:absolute;top:2010px;left:0;width:1200px;height:420px;clip-path:polygon(0 10%,100% 0,100% 100%,0 100%);background:linear-gradient(180deg,#2e9fd4 0%,#1f8cc5 100%)}
.cta-photo{position:absolute;left:640px;top:0;width:560px;height:100%;background:linear-gradient(90deg,rgba(43,170,223,0) 0%,rgba(120,195,228,.5) 45%,rgba(160,210,232,.6) 100%)}
.cta-copy{position:absolute;left:120px;top:170px;color:var(--white)}
.cta-copy h2{font-family:"Montserrat",sans-serif;font-weight:800;font-size:34px;line-height:1.25;width:460px}
.cta-copy .btn{margin-top:24px}

/* Footer */
.site-footer{position:absolute;top:2420px;left:0;width:1200px;height:256px;background:var(--navy-deep);color:#c9d6de}
.footer-cols{position:absolute;top:34px;left:120px;right:120px;display:flex;justify-content:space-between}
.footer-about{width:270px}
.footer-about .brand{font-size:16px}
.footer-about p{margin-top:14px;font-size:11.5px;line-height:1.6;width:230px}
.footer-col h4{font-family:"Montserrat",sans-serif;font-weight:700;font-size:15px;color:var(--white);margin-bottom:14px}
.footer-col li{list-style:none;font-size:11.5px;margin-bottom:10px;display:flex;align-items:center;gap:9px}
.dot{width:14px;height:14px;border-radius:50%;background:var(--sky);flex:none}
.copyright{position:absolute;bottom:0;left:0;width:1200px;height:36px;border-top:1px solid rgba(255,255,255,.12);display:flex;align-items:center;justify-content:center;font-size:11px}
</style>
</head>
<body>

<div class="hero-strip"></div>
<section class="hero">
  <div class="hero-photo" role="img" aria-label="Modern self storage facility with rows of roll-up doors"></div>
  <div class="hero-shade"></div>
  <div class="hero-copy">
    <h1>From Concept to Capacity – Your Self Storage Experts</h1>
    <p>Keelbrook Vault Holdings delivers turnkey design, construction, leasing, and management services for profitable self storage operations.</p>
    <a class="btn btn-sky" href="#services">Explore Our Services
      <svg width="12" height="10" viewBox="0 0 12 10"><path d="M1 5h9M6 1l4 4-4 4" stroke="#fff" stroke-width="1.6" fill="none"/></svg></a>
  </div>
</section>
<div class="hero-badge"><svg width="16" height="16" viewBox="0 0 16 16"><path d="M3 4l5 4 5-4M3 9l5 4 5-4" stroke="#fff" stroke-width="1.8" fill="none"/></svg></div>

<header class="site-header">
  <div class="brand"><span class="brand-mark"></span>Keelbrook Vault Holdings</div>
  <nav class="main-nav"><span class="active">Home</span><span>About Us</span><span>Services</span><span>Contact</span></nav>
  <a class="btn btn-header" href="#contact">Get Started
    <svg width="12" height="10" viewBox="0 0 12 10"><path d="M1 5h9M6 1l4 4-4 4" stroke="#fff" stroke-width="1.6" fill="none"/></svg></a>
</header>

<section class="services" id="services">
  <h2 class="section-title">Services</h2>
  <div class="service-list">
    <div class="service">
      <div class="hex"><svg width="34" height="34" viewBox="0 0 34 34" fill="none" stroke="#fff" stroke-width="2.2"><path d="M5 29L22 12l5 5-17 17H5z"/><path d="M6 4h10v6M6 4v24"/></svg></div>
      <h3>Facility Design &amp;<br>Development</h3>
    </div>
    <div class="service">
      <div class="hex"><svg width="34" height="34" viewBox="0 0 34 34" fill="none" stroke="#fff" stroke-width="2.4"><path d="M8 26L22 12M22 12a6 6 0 1 0 6-6l-3 3-3-1-1-3 3-3"/><path d="M26 26L10 10M8 6l4 4-2 2-4-4z"/></svg></div>
      <h3>Construction &amp;<br>Build Management</h3>
    </div>
    <div class="service">
      <div class="hex"><svg width="34" height="34" viewBox="0 0 34 34" fill="#fff"><rect x="5" y="20" width="5" height="9"/><rect x="13" y="15" width="5" height="14"/><rect x="21" y="9" width="5" height="20"/><path d="M5 14l8-6 6 4 9-7" stroke="#fff" stroke-width="2" fill="none"/></svg></div>
      <h3>Lease-Up<br>&amp; Marketing</h3>
    </div>
    <div class="service">
      <div class="hex"><svg width="34" height="34" viewBox="0 0 34 34" fill="none" stroke="#fff" stroke-width="2.2"><path d="M4 14L17 5l13 9v15H4z"/><path d="M10 29V18h14v11M10 22h14M10 25h14"/></svg></div>
      <h3>Ongoing Facility<br>Management</h3>
    </div>
  </div>
  <a class="btn btn-dark" href="#services">Explore Our Services
    <svg width="12" height="10" viewBox="0 0 12 10"><path d="M1 5h9M6 1l4 4-4 4" stroke="#fff" stroke-width="1.6" fill="none"/></svg></a>
</section>

<section class="about">
  <div class="about-photo" role="img" aria-label="Faded view of a self storage building exterior"></div>
  <div class="about-copy">
    <h2>About us</h2>
    <p>At Keelbrook Vault Holdings, we are more than developers — we are your partners in creating profitable, modern, and efficient self storage facilities. Based in Edmonton, Alberta, we provide end-to-end services that take your project from concept to capacity, combining industry expertise, smart design, and operational excellence to deliver outstanding results.</p>
    <p>Our team brings decades of combined experience in real estate development, construction management, and storage operations. We understand the challenges investors and developers face, and we guide them through every step, from identifying the right site to managing day-to-day performance, so every facility reaches its full potential.</p>
    <a class="btn btn-dark" href="#about">Learn More
      <svg width="12" height="10" viewBox="0 0 12 10"><path d="M1 5h9M6 1l4 4-4 4" stroke="#fff" stroke-width="1.6" fill="none"/></svg></a>
  </div>
</section>

<section class="projects">
  <h2 class="section-title">Featured Project</h2>
  <p class="lead">From groundbreaking to grand opening, Keelbrook Vault Holdings delivers profitable, modern and high-performing storage facilities.</p>
  <div class="slider-arrow" style="left:74px"><svg width="10" height="10" viewBox="0 0 10 10"><path d="M7 1L3 5l4 4" stroke="#5b6a75" stroke-width="1.6" fill="none"/></svg></div>
  <div class="project-row">
    <article class="project">
      <div class="project-photo" role="img" aria-label="Project team reviewing construction plans" style="background:linear-gradient(135deg,#7d97a8,#c9d7e0)"></div>
      <div class="project-meta"><span>● Calgary, Alberta</span><span>Size: 400 units · 80,000 sq ft</span></div>
      <h3>Full design, construction oversight, lease-up strategy</h3>
    </article>
    <article class="project">
      <div class="project-photo" role="img" aria-label="Engineers discussing site plans at a desk" style="background:linear-gradient(135deg,#5f85a3,#b4cadb)"></div>
      <div class="project-meta"><span>● Calgary, Alberta</span><span>Size: 400 units · 80,000 sq ft</span></div>
      <h3>Site planning, architectural &amp; ongoing facility management</h3>
    </article>
    <article class="project">
      <div class="project-photo" role="img" aria-label="Architectural drawings and tools on a table" style="background:linear-gradient(135deg,#a38f78,#e4ddd2)"></div>
      <div class="project-meta"><span>● Red Deer, Alberta</span><span>Size: 320 units · 64,000 sq ft</span></div>
      <h3>Feasibility study, redevelopment planning, lease-up marketing</h3>
    </article>
  </div>
  <div class="slider-arrow" style="left:1096px"><svg width="10" height="10" viewBox="0 0 10 10"><path d="M3 1l4 4-4 4" stroke="#5b6a75" stroke-width="1.6" fill="none"/></svg></div>
</section>

<section class="cta" id="contact">
  <div class="cta-photo" role="img" aria-label="Photo of a construction manager in hard hat and safety vest in front of a storage facility"></div>
  <div class="cta-copy">
    <h2>Ready to build your next self storage project?</h2>
    <a class="btn btn-dark" href="#contact">Let's talk
      <svg width="12" height="10" viewBox="0 0 12 10"><path d="M1 5h9M6 1l4 4-4 4" stroke="#fff" stroke-width="1.6" fill="none"/></svg></a>
  </div>
</section>

<footer class="site-footer">
  <div class="footer-cols">
    <div class="footer-about">
      <div class="brand"><span class="brand-mark"></span>Keelbrook Vault Holdings</div>
      <p>Your trusted partner in turnkey self storage development, from concept and construction to lease-up and profitable long-term operations.</p>
    </div>
    <div class="footer-col">
      <h4>Contact Us</h4>
      <ul>
        <li><span class="dot"></span>40837 52 Ave, Edmonton, AB T6K 3R8</li>
        <li><span class="dot"></span>info@keelbrookvault.net</li>
        <li><span class="dot"></span>www.keelbrookvault.net</li>
      </ul>
    </div>
    <div class="footer-col">
      <h4>Company</h4>
      <ul><li>Home</li><li>About Us</li><li>Services</li><li>Contact</li></ul>
    </div>
    <div class="footer-col">
      <h4>Follow Us</h4>
      <ul>
        <li><span class="dot"></span>Fieldpost</li>
        <li><span class="dot"></span>Chirpline</li>
        <li><span class="dot"></span>Workline</li>
      </ul>
    </div>
  </div>
  <div class="copyright">Copyright © 2025 keelbrookvault.net | All Rights Reserved.</div>
</footer>

</body>
</html>
```